Re-design of current business cards

We are updating our website with new colors and layout. Would like to re-design our business cards to co-ordinate. See attached pdf with new Brindlecraft website colors. We would also like to combine our 2 brands on the one business card. Attached is the new design for our Brindlecraft website, current business cards, which are one sided, brindlecraft logo in tiff, .ai for fonts. Brindlecraft logo font is Optimum, Quillmarsh website home page image, Quillmarsh brand statics for products which includes the logo for this brand.

Quillmarsh brand will stay the dark gray on the website. See attached statics for product and website home page.
Updates

The business cards will be 2 sided. Brindlecraft Brand on one side and Quillmarsh Brand on the other. The colors for Brindlecraft need to follow the color scheme of the brindlecraft website pdf I uploaded. The colors are a blue, lighter teal blue and white. Quillmarsh needs to follow the dark gray color on files uploaded

Target Market(s)

The trade and consumers

Industry/Entity Type

Home Furnishing

Contact Information for Business Card

We are updating our website with new colors and layout. Would like to re-design our business cards to co-ordinate. We would also like to combine our 2 brands onto 1 2 sided business cards.

Requirements
Must have
• Colors that match our new website, see attached image.
• RGB colors
• navy -#152842
• teal - 98aeb9
• The gray color used for Quillmarsh brands.
• ll logos and fonts should stay the same.

```html
<!DOCTYPE html>
<html lang="en">
<head>
<meta charset="utf-8">
<title>Quillmarsh / Brindlecraft Business Card</title>
<link rel="stylesheet" href="https://fonts.googleapis.com/css2?family=Marcellus&family=Roboto+Condensed:wght@300&family=Didact+Gothic&family=Montserrat:wght@700&display=swap">
<style>
  :root {
    --stage: #808080;
    --paper: #e5e5e5;
    --quill-gray: #58595b;
    --quill-text: #ececec;
    --navy: #152842;
    --teal: #98aeb9;
    --ink-soft: #4a4f57;
    --rule: #b9bcbf;
  }
  html, body {
    margin: 0;
    padding: 0;
    width: 1200px;
    height: 1200px;
    overflow: hidden;
    background: var(--stage);
  }
  .canvas { display: block; width: 1200px; height: 1200px; }
  .card-paper { fill: var(--paper); }
  .quill-panel { fill: var(--quill-gray); }
  .quill-wordmark { font-family: "Marcellus", serif; font-size: 92px; fill: var(--quill-text); text-transform: uppercase; }
  .quill-byline { font-family: "Marcellus", serif; font-size: 19px; fill: var(--quill-text); }
  .quill-tagline { font-family: "Roboto Condensed", sans-serif; font-weight: 300; font-size: 37px; fill: var(--quill-text); }
  .brand-mark { fill: var(--teal); }
  .brand-name { font-family: "Marcellus", serif; font-size: 38px; fill: var(--navy); }
  .brand-web { font-family: "Montserrat", sans-serif; font-weight: 700; font-size: 7px; fill: var(--navy); }
  .brand-tagline { font-family: "Roboto Condensed", sans-serif; font-weight: 300; font-size: 14px; fill: var(--teal); }
  .person-name { font-family: "Didact Gothic", sans-serif; font-size: 34px; fill: var(--navy); letter-spacing: -2px; }
  .person-title { font-family: "Didact Gothic", sans-serif; font-size: 18px; fill: var(--ink-soft); letter-spacing: -0.6px; }
  .name-rule { stroke: var(--rule); stroke-width: 1; }
  .contact-band { fill: var(--teal); }
  .band-base { stroke: var(--navy); stroke-width: 3; }
  .band-divider { stroke: var(--ink-soft); stroke-width: 1; opacity: 0.6; }
  .contact-text { font-family: "Didact Gothic", sans-serif; font-size: 18.5px; fill: var(--ink-soft); letter-spacing: -0.5px; }
  .contact-label { font-family: "Montserrat", sans-serif; font-weight: 700; font-size: 15px; fill: var(--navy); }
  .pin-icon { fill: var(--navy); }
</style>
</head>
<body>
<svg class="canvas" viewBox="0 0 1200 1200" xmlns="http://www.w3.org/2000/svg">
  <!-- Front: Quillmarsh side -->
  <g class="card card-front">
    <rect class="card-paper" x="181" y="79" width="840" height="480"/>
    <rect class="quill-panel" x="241" y="137" width="720" height="369" rx="34"/>
    <text class="quill-wordmark" x="858" y="305" text-anchor="end" textLength="534" lengthAdjust="spacingAndGlyphs">Quillmarsh</text>
    <text class="quill-byline" x="858" y="326" text-anchor="end">by BRINDLECRAFT</text>
    <text class="quill-tagline" x="592" y="435" text-anchor="middle">Discover the luxury of home.</text>
  </g>

  <!-- Back: Brindlecraft side -->
  <g class="card card-back">
    <rect class="card-paper" x="181" y="614" width="840" height="480"/>

    <g class="brand-lockup">
      <circle class="brand-mark" cx="845" cy="674" r="19"/>
      <text class="brand-name" x="844" y="728" text-anchor="middle" textLength="208" lengthAdjust="spacingAndGlyphs">BRINDLECRAFT</text>
      <text class="brand-web" x="844" y="745" text-anchor="middle">www.brindlecraft.com</text>
      <text class="brand-tagline" x="846" y="775" text-anchor="middle">Discover the luxury of home.</text>
    </g>

    <g class="person">
      <text class="person-name" x="255" y="822">MARLA PENWICK</text>
      <text class="person-title" x="234" y="850">GRAPHIC/PHOTOGRAPHY DIRECTOR</text>
      <line class="name-rule" x1="222" y1="865" x2="533" y2="865"/>
    </g>

    <g class="contact">
      <rect class="contact-band" x="210" y="904" width="781" height="154" rx="36"/>
      <line class="band-base" x1="210" y1="1059.5" x2="992" y2="1059.5"/>
      <line class="band-divider" x1="601" y1="922" x2="601" y2="1050"/>

      <g class="pin-icon" transform="translate(238 940) rotate(-45)">
        <rect x="-5" y="-9" width="10" height="4" rx="1"/>
        <path d="M-3 -5 h6 l2 8 h-10 z"/>
        <rect x="-0.8" y="3" width="1.6" height="12"/>
      </g>
      <text class="contact-text" x="264" y="961">PO BOX 210/4417 MEADOW LARK RD</text>
      <text class="contact-text" x="264" y="994">BRIGHTON FALLS, VIRGINIA 24000</text>

      <text class="contact-label" x="627" y="942">P</text>
      <text class="contact-text" x="677" y="944">555.014.2208</text>
      <text class="contact-label" x="627" y="992">F</text>
      <text class="contact-text" x="677" y="994">555.014.2291</text>
      <text class="contact-label" x="627" y="1039">E</text>
      <text class="contact-text" x="677" y="1041">mpenwick@brindlecraft.com</text>
    </g>
  </g>
</svg>
</body>
</html>
```